Halvard Atelier Business cards

Design our business cards and eventually a logo. The company is based in Paris, its activity is the retailing via internet of luxury home furniture (like Vambrelli, Bercusa, tarvoni...) Our clients are international andwith a high sense of aesthetics. The design shall communicate wealth and trust with a high quality and aesthetic sense, pure lines Company Name is Halvard AtelierExplanation of the name: usually people who wants to buy furniture usually go in a showroom. Today they go in showroom to test the furniture and they search for the price on internet, which is a "Halvard atelier".We will not be a e-commerce site. Our site will be (another project) a presentation site which purpose is to reach qualified prospects. Then everything will be handled by phone, meeting etc.The business card must be professional as we will negotiate with many luxury brands, opportunity to represent them on our site, prices etc.As far as the color are concerned mostly black and whithe or grey. The font of the Halvard Atelier name shall have some impact.

Target Market(s)

High-end furniture and buyers of luxury goods, international customers, mostly women who handle such projects.
We also deal with professional buyers (hotels as an example) and luxury brands

Contact Information for Business Card

standard format 85x55, lanscape card, square corners will be printed on thick high quality paper (300 or 350g)

Font styles to use
Sans Serif

Colors

Designer to choose colors to be used in the design.

Requirements
Must have
• Must be white, as the paper will be high quality, the paper will enhance the card.
• Name of the brand Halvard atelier (with specific font which make it very nice looking and catch the attention. similar to Calibri or Calibri
• Name of person (will give you the name later (4 names and position)
• the position of the person
• Mobile phone, e-mail, Physical address 27, rue Fenouillard, 75005 Paris, France (courrier only) our web site www.halvardatelier.fr
• The card must be simple and class
Nice to have
• Font of the address is smaller than the rest,
• Calibri font or similar on recto side with the name of the company which may look similar to the picture inserted in the brief.
• The grey color in the picture inserted is ok for us
Should not have
• Any parallel lines which represent the name of the company
• Any heavy design If you go on internet sites which present the furniture all designs are pure lines and high quality craftsmanship. To have an idea of our targetted client or brand we will be in touch: https://www.casavelumi.it/projects/
• Note that the picture added below is what we use, now as mail signature, up to you to have a better design etc.

```html
<!DOCTYPE html>
<html lang="en">
<head>
<meta charset="utf-8">
<title>Halvard Atelier – Business Card</title>
<link href="https://fonts.googleapis.com/css2?family=Barlow:wght@400;600&display=swap" rel="stylesheet">
<style>
  :root {
    --page: #ffffff;
    --card-edge: #d9d9d9;
    --tone-light: #fbfbfb;
    --tone-mid: #ececec;
    --tone-deep: #dedede;
    --ink: #2b2b2b;
    --ink-soft: #555555;
  }
  * { box-sizing: border-box; margin: 0; padding: 0; }
  html, body {
    width: 899px;
    height: 1200px;
    overflow: hidden;
    background: var(--page);
    font-family: "Barlow", Arial, sans-serif;
    color: var(--ink);
  }
  .canvas { position: relative; width: 899px; height: 1200px; }

  .card {
    position: absolute;
    left: 26px;
    width: 846px;
    height: 547px;
    border: 1px solid var(--card-edge);
    overflow: hidden;
    background: var(--tone-light);
  }
  .card--front { top: 22px; }
  .card--back { top: 624px; }

  .card__texture {
    position: absolute;
    inset: 0;
    background:
      radial-gradient(ellipse at 20% 30%, var(--tone-mid) 0%, transparent 55%),
      radial-gradient(ellipse at 85% 90%, var(--tone-deep) 0%, transparent 50%),
      linear-gradient(135deg, var(--tone-mid) 0%, var(--tone-light) 45%, var(--tone-mid) 100%);
  }

  /* Front */
  .brand {
    position: absolute;
    left: 230px;
    top: 205px;
    width: 370px;
    text-align: center;
    font-weight: 400;
    color: var(--ink);
  }
  .brand__name {
    display: block;
    font-size: 64px;
    line-height: 1;
    letter-spacing: 2px;
  }
  .brand__line {
    display: block;
    margin-top: 12px;
    font-size: 17px;
    letter-spacing: 15px;
    padding-left: 15px;
  }

  /* Back */
  .person {
    position: absolute;
    right: 92px;
    top: 90px;
    text-align: right;
  }
  .person__name {
    font-size: 46px;
    line-height: 1;
    font-weight: 400;
    letter-spacing: 0.5px;
  }
  .person__first { font-weight: 600; }
  .person__role {
    margin-top: 4px;
    font-size: 21px;
    letter-spacing: 4px;
    color: var(--ink-soft);
  }

  .contacts {
    position: absolute;
    right: 24px;
    top: 232px;
    list-style: none;
  }
  .contacts__item {
    display: flex;
    justify-content: flex-end;
    align-items: center;
    height: 41px;
    font-size: 25px;
    color: var(--ink);
  }
  .contacts__icon {
    width: 22px;
    height: 22px;
    margin-left: 18px;
    margin-right: 14px;
    fill: var(--ink);
  }
  .address {
    position: absolute;
    right: 92px;
    top: 378px;
    font-size: 22px;
    color: var(--ink);
  }
</style>
</head>
<body>
<main class="canvas">

  <section class="card card--front">
    <div class="card__texture" role="img" aria-label="Soft light grey hexagonal honeycomb texture"></div>
    <h1 class="brand">
      <span class="brand__name">HALVARD</span>
      <span class="brand__line">ATELIER</span>
    </h1>
  </section>

  <section class="card card--back">
    <div class="card__texture" role="img" aria-label="Soft light grey hexagonal honeycomb texture"></div>

    <div class="person">
      <h2 class="person__name"><span class="person__first">MATHIS</span> DROUVENNE</h2>
      <p class="person__role">PRESIDENT</p>
    </div>

    <ul class="contacts">
      <li class="contacts__item">+336 4817 2093
        <svg class="contacts__icon" viewBox="0 0 24 24" aria-hidden="true"><path d="M6.6 10.8c1.4 2.8 3.8 5.1 6.6 6.6l2.2-2.2c.3-.3.7-.4 1-.2 1.1.4 2.3.6 3.6.6.6 0 1 .4 1 1V20c0 .6-.4 1-1 1C10.6 21 3 13.4 3 4c0-.6.4-1 1-1h3.5c.6 0 1 .4 1 1 0 1.3.2 2.5.6 3.6.1.3 0 .7-.2 1l-2.3 2.2z"/></svg>
      </li>
      <li class="contacts__item">name@halvard.com
        <svg class="contacts__icon" viewBox="0 0 24 24" aria-hidden="true"><path d="M2 5h20v14H2z" fill="none"/><path d="M2 5h20v2l-10 6L2 7zM2 9l10 6 10-6v10H2z"/></svg>
      </li>
      <li class="contacts__item">www.halvardatelier.fr
        <svg class="contacts__icon" viewBox="0 0 24 24" aria-hidden="true"><circle cx="12" cy="12" r="10"/><path d="M3 10h18v1.5H3zM3 13.5h18V15H3z" fill="#f0f0f0"/></svg>
      </li>
    </ul>

    <p class="address">27 rue Fenouillard, 75005 Paris, France</p>
  </section>

</main>
</body>
</html>
```